Law Office business card design

I have a general practice specializing in criminal defense work and domestic cases. I have extensive trial and appellate experience.

Target Market(s)

general public

Industry/Entity Type

Defense

Contact Information for Business Card

Darrowby Law Office, P.A.
382 N. 4th
PO Box 5274
Salina, KS 67409-5274
(785) 555-0172
(785) 555-0198 FAX
tdarrow@plinkmail.example

Requirements
Must have
• A symbol that immediately identifes the card as a legal practice.

```html
<!DOCTYPE html>
<html lang="en">
<head>
<meta charset="utf-8">
<title>Darrowby Law Office – Business Card</title>
<link rel="stylesheet" href="https://fonts.googleapis.com/css2?family=Comfortaa:wght@700&family=Nunito+Sans:wght@400;700&display=swap">
<style>
  :root {
    --page: #ffffff;
    --card-light: #e7e6e3;
    --plum: #4f4356;
    --ink-grey: #666467;
    --ink-white: #ffffff;
  }
  * { box-sizing: border-box; margin: 0; padding: 0; }
  html, body {
    width: 1200px;
    height: 900px;
    overflow: hidden;
    background: var(--page);
  }
  .canvas {
    position: relative;
    width: 1200px;
    height: 900px;
  }
  .card {
    position: absolute;
    left: 270px;
    width: 720px;
    height: 409px;
  }
  .card--front {
    top: 36px;
    background: var(--card-light);
  }
  .card--back {
    top: 463px;
    background: var(--plum);
    display: flex;
    align-items: center;
    justify-content: center;
  }
  .brand-mark {
    position: absolute;
    left: 66px;
    top: 140px;
    width: 56px;
    height: 56px;
    background: var(--plum);
  }
  .identity {
    position: absolute;
    left: 210px;
    top: 116px;
  }
  .firm-name {
    font-family: "Comfortaa", "Nunito Sans", sans-serif;
    font-weight: 700;
    font-size: 47px;
    line-height: 1;
    letter-spacing: 1px;
    color: var(--plum);
  }
  .firm-type {
    margin-top: 8px;
    font-family: "Nunito Sans", sans-serif;
    font-size: 29px;
    line-height: 1.1;
    color: var(--ink-grey);
  }
  .address {
    margin-top: 20px;
    font-family: "Nunito Sans", sans-serif;
    font-size: 20px;
    line-height: 1.25;
    color: var(--ink-grey);
  }
  .contact {
    margin-top: 25px;
    list-style: none;
    font-family: "Nunito Sans", sans-serif;
    font-size: 20px;
    line-height: 25px;
    color: var(--ink-grey);
  }
  .contact__label { font-weight: 700; }
  .back-name {
    font-family: "Comfortaa", "Nunito Sans", sans-serif;
    font-weight: 700;
    font-size: 56px;
    letter-spacing: 2px;
    color: var(--ink-white);
  }
</style>
</head>
<body>
  <main class="canvas">
    <section class="card card--front" aria-label="Card front">
      <div class="brand-mark" aria-hidden="true"></div>
      <div class="identity">
        <h1 class="firm-name">DARROWBY</h1>
        <p class="firm-type">LAW OFFICE</p>
        <p class="address">P.A. 382 N. 4th PO Box 5274 Salina KS</p>
        <ul class="contact">
          <li><span class="contact__label">TEL:</span> 67409-5274 (785) 555-0172</li>
          <li><span class="contact__label">FAX:</span> (785) 555-0198</li>
          <li><span class="contact__label">E:</span> tdarrow@plinkmail.example</li>
        </ul>
      </div>
    </section>
    <section class="card card--back" aria-label="Card back">
      <p class="back-name">DARROWBY</p>
    </section>
  </main>
</body>
</html>
```